Website Velmoraq Athletics

Velmoraq Athletics needs an update for our corporate website www.velmoraqathletics.com.
We feel the current website is too cluttered with various bits and pecies and strive to a more simpler, easier to navigate website.
We encourage designers to start with a blank canvas, but few aspects of the current website should remain:
- The four lines of business: Sports Media Services, Sports Content Services, Sports Event Services and Sports Federation Services should have a central place on the new site.
- The colour scheme of our house style (black, white and grey/silver) needs to be honoured.
- Our logo should remain as it is (with background intact). Focus on our preferred company logo, found here: http://www.velmoraqathletics.com/download/logos/JPEG/VA_logo_on_white.jpg
- A place where visitors can view the latest company headlines. Only the headlines will suffice.
- It should be clear that Velmoraq Athletics is a sports company. An inventive way of linking our ability of providing sports data with sports images would highly appreciated.
All other components of the current website can remain or be removed/tweaked as the designer pleases. We are open to a complete new look and feel.
A redesign of the homepage should have your focus, but it would be great if the frame work of the design is usable for the other pages of our website as well.
Velmoraq Athletics keywords that reflect on our company: fast, accurate, innovative, intelligent, no-nonsense, business-aimed, passionate about sports, global, modern.
Target Market(s)
international media (tv stations, newspapers), sports federations, olympic committees, sports results websites, sport app builders
Look and feel

```html
<!DOCTYPE html>
<html lang="en">
<head>
<meta charset="utf-8">
<title>Velmoraq Athletics</title>
<link rel="stylesheet" href="https://fonts.googleapis.com/css2?family=Arimo:wght@400;700&display=swap">
<style>
  :root {
    --page-bg: #4b4b4b;
    --header-dark: #3a3a3a;
    --header-edge: #2a2a2a;
    --panel-light: #e2e2e2;
    --services-bg: #676767;
    --services-rule: #9a9a9a;
    --text-white: #ffffff;
    --text-soft: #eeeeee;
    --text-dark: #2b2b2b;
    --text-body: #444444;
    --text-muted: #777777;
    --badge-bg: #ffffff;
    --badge-shape: #c9c9c9;
    --logo-silver-1: #f4f4f4;
    --logo-silver-2: #b9b9b9;
    --logo-ink: #1e1e1e;
  }
  * { box-sizing: border-box; margin: 0; padding: 0; }
  html, body { width: 976px; height: 1200px; overflow: hidden; }
  body {
    background: var(--page-bg);
    font-family: "Arimo", Arial, sans-serif;
    position: relative;
  }
  a { color: inherit; text-decoration: none; }

  /* Header */
  .site-header {
    position: absolute; left: 17px; top: 14px; width: 915px; height: 143px;
    background: linear-gradient(180deg, #2f2f2f, var(--header-dark));
    border-radius: 14px 14px 6px 6px;
    border: 1px solid var(--header-edge);
  }
  .main-nav {
    position: absolute; top: 36px; left: 0; right: 0;
    font-size: 14px; font-weight: 700; color: var(--text-white);
  }
  .main-nav a { position: absolute; }
  .brand-banner {
    position: absolute; left: 31px; top: 74px; width: 912px; height: 83px;
    border-radius: 6px; overflow: hidden; display: flex;
    border: 1px solid #222;
  }
  .brand-plate {
    width: 460px; height: 100%;
    background: linear-gradient(90deg, var(--logo-silver-1), var(--logo-silver-2));
    display: flex; align-items: center; padding-left: 34px;
  }
  .brand-name {
    font-size: 34px; font-weight: 700; color: var(--logo-ink); letter-spacing: 0.5px;
  }
  .stadium-visual {
    flex: 1; height: 100%;
    background: radial-gradient(ellipse at 60% 20%, #9a9a9a, #4a4a4a 55%, #262626);
  }

  /* Content panel */
  .content-panel {
    position: absolute; left: 31px; top: 180px; width: 915px; height: 985px;
    background: var(--panel-light); border-radius: 8px;
  }

  /* Services */
  .services-box {
    position: absolute; left: 46px; top: 193px; width: 886px; height: 407px;
    background: var(--services-bg); border-radius: 6px; color: var(--text-white);
  }
  .service {
    position: absolute; left: 18px; width: 628px;
  }
  .service h2 { font-size: 24px; font-weight: 400; }
  .service p { font-size: 14px; margin-top: 7px; color: var(--text-soft); }
  .service .read-more { font-size: 11px; margin-top: 4px; display: block; color: var(--text-soft); }
  .service-rule {
    position: absolute; left: 18px; width: 628px; height: 1px; background: var(--services-rule);
  }
  .partner-badges { position: absolute; left: 429px; display: flex; gap: 7px; }
  .partner-badge {
    width: 61px; height: 42px; background: var(--badge-bg); border: 1px solid #aaa;
    display: flex; align-items: center; justify-content: center;
  }
  .partner-badge span { width: 34px; height: 22px; background: var(--badge-shape); border-radius: 3px; }

  .events {
    position: absolute; left: 690px; top: 32px; width: 180px;
  }
  .events h3 { font-size: 16px; font-weight: 700; line-height: 1.2; }
  .event { position: absolute; left: 0; width: 180px; }
  .event h4 { font-size: 13px; font-weight: 700; color: var(--text-soft); }
  .event p { font-size: 10.5px; line-height: 1.45; margin-top: 7px; color: var(--text-soft); }

  /* News */
  .news-item { position: absolute; left: 64px; width: 840px; height: 110px; }
  .news-photo { position: absolute; left: 0; top: 0; width: 155px; height: 104px; }
  .news-text { position: absolute; left: 185px; top: -8px; width: 655px; }
  .news-text h3 { font-size: 17px; font-weight: 700; color: var(--text-dark); letter-spacing: 0.3px; }
  .news-text p { font-size: 11px; line-height: 15px; color: var(--text-body); margin-top: 4px; }
  .news-extra {
    position: absolute; left: 249px; top: 1034px; font-size: 11px; color: var(--text-body);
  }

  /* Footer */
  .footer-rule {
    position: absolute; left: 110px; top: 1066px; width: 800px; height: 2px;
    background: linear-gradient(90deg, transparent, #c4c4c4 20%, #c4c4c4 80%, transparent);
  }
  .footer-col { position: absolute; top: 1080px; font-size: 11px; color: var(--text-muted); }
  .footer-col h4 { font-size: 12.5px; font-weight: 400; margin-bottom: 10px; }
  .footer-col li { list-style: none; line-height: 1.3; }
  .follow { position: absolute; left: 63px; top: 1114px; font-size: 11px; color: var(--text-dark); }
  .social-links { display: flex; gap: 10px; margin-top: 8px; }
  .social-links span { width: 22px; height: 22px; border-radius: 3px; display: block; }
  .social-a { background: #3b5a9a; }
  .social-b { background: #3fa0d8; }
  .social-c { background: #e98a2a; }
  .social-d { background: #f2f2f2; border: 1px solid #999; }
  .copyright {
    position: absolute; top: 1176px; left: 0; width: 976px; text-align: center;
    font-size: 10.5px; color: var(--text-white);
  }
</style>
</head>
<body>
  <header class="site-header">
    <nav class="main-nav">
      <a href="#" style="left:476px">About us</a>
      <a href="#" style="left:600px">Contact</a>
      <a href="#" style="left:716px">Jobs</a>
      <a href="#" style="left:813px">Web Shop</a>
    </nav>
  </header>
  <div class="brand-banner">
    <div class="brand-plate"><span class="brand-name">Velmoraq Athletics</span></div>
    <div class="stadium-visual" role="img" aria-label="Stadium floodlights shining in a dark arena"></div>
  </div>

  <main class="content-panel"></main>

  <section class="services-box">
    <div class="service" style="top:18px">
      <h2>Sports Media Services</h2>
      <p>Ultimate Sports Intelligence for journalists.</p>
      <a class="read-more" href="#">read more..</a>
      <div class="partner-badges" style="top:0"><div class="partner-badge"><span></span></div><div class="partner-badge"><span></span></div><div class="partner-badge"><span></span></div></div>
    </div>
    <div class="service-rule" style="top:104px"></div>
    <div class="service" style="top:120px">
      <h2>Sports Content Services</h2>
      <p>Fastest richest reliable sports statistics &amp; news channel</p>
      <a class="read-more" href="#">read more..</a>
      <div class="partner-badges" style="top:0"><div class="partner-badge"><span></span></div><div class="partner-badge"><span></span></div><div class="partner-badge"><span></span></div></div>
    </div>
    <div class="service-rule" style="top:203px"></div>
    <div class="service" style="top:218px">
      <h2>Sports Event Services</h2>
      <p>The best media Support an fevent organizer can get</p>
      <a class="read-more" href="#">read more..</a>
      <div class="partner-badges" style="top:5px"><div class="partner-badge"><span></span></div><div class="partner-badge"><span></span></div><div class="partner-badge"><span></span></div></div>
    </div>
    <div class="service-rule" style="top:306px"></div>
    <div class="service" style="top:320px">
      <h2>Sports Federation Services</h2>
      <p>One stop shop media solutions for federations.</p>
      <a class="read-more" href="#">read more..</a>
      <div class="partner-badges" style="top:3px"><div class="partner-badge"><span></span></div><div class="partner-badge"><span></span></div><div class="partner-badge"><span></span></div></div>
    </div>

    <aside class="events">
      <h3>EVENTS<br>we are involved in<br>start in:</h3>
      <div class="event" style="top:80px">
        <h4>Quisque vitae pede.</h4>
        <p>Quisque vitae pede. Nam et augue. Sed a elit. Ut vel massa. Suspendisse nibh pede, ultrices vitae,ultrices nec, mollis non nibh.Quisque vitae pede. Nam et augue.</p>
      </div>
      <div class="event" style="top:230px">
        <h4>Quisque vitae pede.</h4>
        <p>Quisque vitae pede. Nam et augue. Sed a elit. Ut vel massa. Suspendisse nibh pede, ultrices vitae ultrices nec, mollis non nibh. Quisque vitae pede. Nam et augue. Sed a elit. Ut vel massa.</p>
      </div>
    </aside>
  </section>

  <article class="news-item" style="top:639px">
    <div class="news-photo" role="img" aria-label="Tennis player serving on a blue court" style="background:linear-gradient(135deg,#6f8fb8,#2f4f7f 60%,#c59a7a)"></div>
    <div class="news-text">
      <h3>Quisque vitae pede.</h3>
      <p>Quisque vitae pede. Nam et augue. Sed a elit. Ut vel massa. Suspendisse nibh pede, ultrices vitae,ultrices nec, mollis non nibh.Quisque vitae pede. Nam et augue. Sed a elit Ut vel massa. Suspendisse nibh pede, ultrices vitae,ultrices nec, mollis non nibh. Quisque vitae pede. Nam et augue. Sed a elit. Ut vel massa. Suspendisse nibh pede, ultrices vitae ultrices nec, mollis non nibh.Quisque vitae pede. Nam et augue. Sed a elit. Ut vel massa. Suspendisse nibh pede, ultrices vitae ultrices nec, mollis non nibh...</p>
    </div>
  </article>
  <article class="news-item" style="top:790px">
    <div class="news-photo" role="img" aria-label="Tennis player hitting a backhand in front of a blue backdrop" style="background:linear-gradient(135deg,#1f3f9a,#2a56c8 55%,#132766)"></div>
    <div class="news-text">
      <h3>Quisque vitae pede.</h3>
      <p>Quisque vitae pede. Nam et augue. Sed a elit. Ut vel massa. Suspendisse nibh pede, ultrices vitae,ultrices nec, mollis non nibh.Quisque vitae pede. Nam et augue. Sed a elit Ut vel massa. Suspendisse nibh pede, ultrices vitae,ultrices nec, mollis non nibh. Quisque vitae pede. Nam et augue. Sed a elit. Ut vel massa. Suspendisse nibh pede, ultrices vitae ultrices nec, mollis non nibh.Quisque vitae pede. Nam et augue. Sed a elit. Ut vel massa. Suspendisse nibh pede, ultrices vitae ultrices nec, mollis non nibh...</p>
    </div>
  </article>
  <article class="news-item" style="top:933px">
    <div class="news-photo" role="img" aria-label="Racing driver with an umbrella on a rainy track" style="background:linear-gradient(180deg,#d8dde2,#9aa3ab 55%,#6d7479)"></div>
    <div class="news-text">
      <h3>Quisque vitae pede.</h3>
      <p>Quisque vitae pede. Nam et augue. Sed a elit. Ut vel massa. Suspendisse nibh pede, ultrices vitae,ultrices nec, mollis non nibh.Quisque vitae pede. Nam et augue. Sed a elit Ut vel massa. Suspendisse nibh pede, ultrices vitae,ultrices nec, mollis non nibh. Quisque vitae pede. Nam et augue. Sed a elit. Ut vel massa. Suspendisse nibh pede, ultrices vitae ultrices nec, mollis non nibh.Quisque vitae pede. Nam et augue. Sed a elit. Ut vel massa. Suspendisse nibh pede, ultrices vitae ultrices nec, mollis non nibh...</p>
    </div>
  </article>
  <p class="news-extra">Suspendisse nibh pede, ultrices vitae ultrices nec, mollis non nibh.Quisque vitae pede. Nam et augue.</p>

  <footer>
    <div class="footer-rule"></div>
    <div class="follow">Follow us
      <div class="social-links"><span class="social-a"></span><span class="social-b"></span><span class="social-c"></span><span class="social-d"></span></div>
    </div>
    <div class="footer-col" style="left:250px"><h4>Nam et augue</h4><ul><li>Lorem ipsum</li><li>Suspendisse nibh</li><li>Lorem ipsum</li><li>Quisque vitae pede</li></ul></div>
    <div class="footer-col" style="left:407px"><h4>Nam et augue</h4><ul><li>Lorem ipsum</li><li>Suspendisse nibh</li><li>Lorem ipsum</li><li>Quisque vitae pede</li></ul></div>
    <div class="footer-col" style="left:564px"><h4>Nam et augue</h4><ul><li>Lorem ipsum</li><li>Suspendisse nibh</li><li>Lorem ipsum</li><li>Quisque vitae pede</li></ul></div>
    <div class="footer-col" style="left:723px"><h4>Nam et augue</h4><ul><li>Lorem ipsum</li><li>Suspendisse nibh</li><li>Lorem ipsum</li><li>Quisque vitae pede</li></ul></div>
    <p class="copyright">Copyright &copy; 2011 All rights reserved</p>
  </footer>
</body>
</html>
```